Letterhead designs for Property Management firm

Would like to see some different letterhead/envelope designs We are a residential property management company. We would like to see designs that utilize blue/grays/black

```html
<!DOCTYPE html>
<html lang="en">
<head>
<meta charset="utf-8">
<title>Ridgeline Property Management – Stationery</title>
<link href="https://fonts.googleapis.com/css2?family=Fira+Sans+Condensed:wght@400;600&display=swap" rel="stylesheet">
<style>
  :root {
    --bg: #dcdcdc;
    --paper: #ffffff;
    --ink: #3a3a3a;
    --band: #1e1e1e;
    --brand-blue: #1b59a8;
    --rule: #c9c9c9;
  }
  * { box-sizing: border-box; margin: 0; padding: 0; }
  html, body { width: 1200px; height: 1200px; overflow: hidden; }
  body {
    background: var(--bg);
    font-family: "Fira Sans Condensed", sans-serif;
    position: relative;
  }
  .letterhead {
    position: absolute; left: 90px; top: 90px;
    width: 724px; height: 1030px;
    background: var(--paper);
  }
  .envelope {
    position: absolute; left: 244px; top: 434px;
    width: 880px; height: 381px;
    background: var(--paper);
  }
  .footer-band {
    position: absolute; left: 0; right: 0; bottom: 0;
    background: var(--band);
  }
  .letterhead .footer-band { height: 31px; }
  .envelope .footer-band { height: 27px; }

  .brand {
    position: absolute;
    display: flex; align-items: center; gap: 10px;
    color: var(--brand-blue);
    font-weight: 600;
    line-height: 1;
  }
  .brand-mark {
    width: 14px; height: 14px; background: var(--brand-blue); flex: none;
  }
  .brand-name { display: flex; flex-direction: column; }
  .brand-name .main { letter-spacing: 0.5px; }
  .brand-name .sub { letter-spacing: 1px; margin-top: 4px; }

  .letterhead .brand { left: 46px; top: 52px; }
  .letterhead .brand-name .main { font-size: 38px; }
  .letterhead .brand-name .sub { font-size: 14px; }

  .envelope .brand { left: 41px; top: 56px; }
  .envelope .brand-name .main { font-size: 48px; }
  .envelope .brand-name .sub { font-size: 17px; }

  .contact {
    position: absolute; left: 398px; top: 50px;
    border-left: 1px solid var(--rule);
    padding-left: 12px;
    list-style: none;
    color: var(--ink);
    font-size: 13.5px;
  }
  .contact li {
    display: flex; align-items: center; gap: 4px;
    height: 17.5px;
  }
  .contact li.address { margin-top: 4px; }
  .contact svg { width: 12px; height: 12px; fill: var(--brand-blue); flex: none; }

  .return-address {
    position: absolute; left: 40px; top: 318px;
    color: var(--ink);
    font-size: 17px;
  }
</style>
</head>
<body>
  <section class="letterhead" aria-label="Letterhead">
    <div class="brand">
      <span class="brand-mark"></span>
      <span class="brand-name"><span class="main">RIDGELINE</span><span class="sub">PROPERTY MANAGEMENT</span></span>
    </div>
    <ul class="contact">
      <li><svg viewBox="0 0 12 12"><path d="M1 4c0-2 2-3 5-3s5 1 5 3l-2 1-1-2H4L3 5zM3 6h6l1 5H2z"/></svg>1-234-567890</li>
      <li><svg viewBox="0 0 12 12"><circle cx="6" cy="6" r="5.5"/><path d="M3 3l2 1 0 2 2 1-1 3M8 2l1 2 2 1" stroke="#fff" fill="none"/></svg>www.ridgelinepropertymanagement.com</li>
      <li><svg viewBox="0 0 12 12"><path d="M0 2h12v8H0z"/><path d="M0 2l6 5 6-5M0 10l4-4M12 10l-4-4" stroke="#fff" fill="none"/></svg>info@ridgelinepropertymanagement.com</li>
      <li class="address"><svg viewBox="0 0 12 12"><path d="M6 0a4 4 0 0 1 4 4c0 3-4 8-4 8S2 7 2 4a4 4 0 0 1 4-4zm0 2.5a1.5 1.5 0 1 0 0 3 1.5 1.5 0 0 0 0-3z"/></svg>Dummy city, Dummy Country Land Dummy</li>
    </ul>
    <div class="footer-band"></div>
  </section>

  <section class="envelope" aria-label="Envelope">
    <div class="brand">
      <span class="brand-mark"></span>
      <span class="brand-name"><span class="main">RIDGELINE</span><span class="sub">PROPERTY MANAGEMENT</span></span>
    </div>
    <p class="return-address">Dummy city, Dummy Country Land Dummy</p>
    <div class="footer-band"></div>
  </section>
</body>
</html>
```